New Business Card for Innovative Tool Company

We need a new design of business card for our florida based tool manufacturing company. I will attach 2 files that we use for our logo, use whichever you feel works best for the card. Main colours are as per logo, and we can use different shades of black/white/grey for the background.

Contact Information for Business Card

Name/Jobtitle/cell
Corvalen Tools
Suite 212c
4316 Marrowdale Pkw
Orlando, FL32847
USA
name@corvaleninc.example
www.corvaleninc.example

Font styles to use
Sans Serif

Colors

Designer to choose colors to be used in the design.

Requirements
Must have
• Icons for Plazaro, Chirpet, Snapvale, Findlo & Vidstream

```html
<!DOCTYPE html>
<html lang="en">
<head>
<meta charset="utf-8">
<title>Corvalen Tools – Business Card</title>
<link rel="stylesheet" href="https://fonts.googleapis.com/css2?family=Roboto:wght@400;500;700&display=swap">
<style>
  :root {
    --backdrop: #2e2e2f;
    --card-grey: #545456;
    --brand-yellow: #f4ec2e;
    --card-white: #ffffff;
    --ink-dark: #3b3b3d;
    --ink-body: #1f1f20;
    --chip-grey: #4a4a4c;
  }
  * { box-sizing: border-box; margin: 0; padding: 0; }
  html, body {
    width: 1200px; height: 1000px; overflow: hidden;
    background: var(--backdrop);
    font-family: "Roboto", Arial, sans-serif;
  }
  .canvas {
    position: relative; width: 1200px; height: 1000px;
  }
  .card {
    position: absolute; left: 250px; width: 700px; height: 400px;
    border-radius: 28px; overflow: hidden;
  }
  /* Back of card */
  .card-back {
    top: 70px; background: var(--card-grey);
    display: flex; align-items: center; justify-content: center; gap: 18px;
  }
  .brand-dot {
    width: 34px; height: 34px; border-radius: 50%;
    border: 3px solid var(--brand-yellow);
  }
  .brand-name {
    color: var(--brand-yellow); font-weight: 700;
    font-size: 46px; letter-spacing: 1px; text-transform: uppercase;
  }
  /* Front of card */
  .card-front {
    top: 530px; display: flex; background: var(--card-white);
  }
  .front-brand {
    width: 392px; background: var(--card-grey);
    display: flex; align-items: center; justify-content: center; gap: 12px;
  }
  .front-brand .brand-name { font-size: 34px; }
  .front-brand .brand-dot { width: 24px; height: 24px; border-width: 2px; }
  .accent-stripe { width: 10px; background: var(--brand-yellow); }
  .front-contact {
    flex: 1; padding: 70px 0 0 42px; color: var(--ink-body);
  }
  .person-name { font-size: 26px; font-weight: 700; color: var(--ink-dark); }
  .person-title { font-size: 16px; margin-top: 4px; color: var(--ink-dark); }
  .address { font-size: 16px; line-height: 1.3; margin-top: 34px; }
  .contact-line {
    display: flex; align-items: center; gap: 10px;
    font-size: 16px; margin-top: 8px;
  }
  .contact-line svg { width: 14px; height: 14px; flex: none; }
  .social-row {
    display: flex; flex-wrap: wrap; gap: 6px; margin-top: 20px; width: 250px;
  }
  .social-chip {
    background: var(--chip-grey); color: var(--card-white);
    font-size: 11px; font-weight: 500; padding: 4px 9px; border-radius: 12px;
  }
</style>
</head>
<body>
<main class="canvas">
  <section class="card card-back" aria-label="Card back">
    <span class="brand-dot"></span>
    <span class="brand-name">Corvalen Tools</span>
  </section>

  <section class="card card-front" aria-label="Card front">
    <div class="front-brand">
      <span class="brand-dot"></span>
      <span class="brand-name">Corvalen Tools</span>
    </div>
    <div class="accent-stripe"></div>
    <div class="front-contact">
      <h1 class="person-name">Marlow Keene</h1>
      <p class="person-title">Managing Director</p>
      <p class="address">Suite 212c 4316 Marrowdale<br>Pkw Orlando, FL32847 USA</p>
      <p class="contact-line">
        <svg viewBox="0 0 14 14" aria-hidden="true"><rect x="1" y="3" width="12" height="8" rx="1" fill="#555"/><path d="M1.5 3.5 7 8l5.5-4.5" stroke="#fff" stroke-width="1.2" fill="none"/></svg>
        name@corvaleninc.example
      </p>
      <p class="contact-line">
        <svg viewBox="0 0 14 14" aria-hidden="true"><circle cx="7" cy="7" r="6" fill="none" stroke="#555" stroke-width="1.3"/><ellipse cx="7" cy="7" rx="2.6" ry="6" fill="none" stroke="#555" stroke-width="1.1"/><path d="M1 7h12" stroke="#555" stroke-width="1.1"/></svg>
        www.corvaleninc.example
      </p>
      <div class="social-row">
        <span class="social-chip">Plazaro</span>
        <span class="social-chip">Chirpet</span>
        <span class="social-chip">Vidstream</span>
        <span class="social-chip">Findlo</span>
        <span class="social-chip">Snapvale</span>
      </div>
    </div>
  </section>
</main>
</body>
</html>
```